Harborline Ambulatory Flyer

Need to make a flyer similar to the attached Glenmark pdfs for Harborline Ambulatory. The write up is attached or can be found at https://www.velmontcareasc.com/bronx

Requirements
Must have
• What the existing flyer has.

```html
<!DOCTYPE html>
<html lang="en">
<head>
<meta charset="utf-8">
<title>Harborline Ambulatory Surgery Center Flyer</title>
<link href="https://fonts.googleapis.com/css2?family=Arimo:wght@400;700&family=Barlow:wght@700&display=swap" rel="stylesheet">
<style>
:root{
  --backdrop:#1b1b1b;
  --paper:#ffffff;
  --ink:#1a1a1a;
  --navy:#1f3c8f;
  --rule:#2f5db4;
  --photo-street:#9a9a96;
  --photo-room:#c9ced3;
  --map-tone-a:#e4e2dc;
  --map-tone-b:#d8dbd2;
}
*{box-sizing:border-box;margin:0;padding:0}
html,body{width:1200px;height:1200px;overflow:hidden;background:var(--backdrop)}
body{position:relative;font-family:"Arimo",Arial,sans-serif;color:var(--ink)}
.page{position:absolute;background:var(--paper)}
.page-front{left:49px;top:219px;width:536px;height:736px}
.page-back{left:610px;top:219px;width:540px;height:743px}
.abs{position:absolute}

.brand{display:flex;align-items:center;gap:12px;font-weight:700;color:var(--navy);letter-spacing:.5px}
.brand-mark{background:var(--navy);flex:none}
.brand-main{left:110px;top:48px;font-size:28px;line-height:1.1}
.brand-main .brand-mark{width:22px;height:70px}
.header-rule{left:0;top:124px;width:536px;height:4px;background:var(--rule)}

.intro{left:51px;top:150px;width:445px;font-size:15px;line-height:18.7px}
.intro .name{color:var(--navy)}

.photo{border:1.5px solid #111;border-radius:8px}
.photo-building{left:79px;top:221px;width:185px;height:119px;background:linear-gradient(160deg,#c7c9cc,var(--photo-street) 55%,#5f6266)}
.photo-or{left:282px;top:221px;width:182px;height:119px;background:linear-gradient(180deg,#e5e8ea,var(--photo-room) 60%,#8c99a6)}

.section-title{font-size:14.5px;font-weight:700;color:var(--navy);line-height:18px;letter-spacing:.2px}
.section-body{font-size:13.6px;line-height:17.7px;text-align:justify}
.loc-title{left:53px;top:356px}
.loc-body{left:53px;top:381px;width:438px}
.cap-title{left:53px;top:461px;width:400px}
.cap-body{left:53px;top:505px;width:438px}

.lead{left:55px;top:66px;width:441px;font-size:16px;line-height:18.8px;text-align:justify}
.offer-title{left:54px;top:247px;font-family:"Barlow",sans-serif;font-weight:700;font-size:18.5px;color:#222}
.services{left:53px;top:279px;width:450px;display:grid;grid-template-columns:246px 1fr;row-gap:12px;list-style:none}
.services li{display:flex;align-items:center;gap:7px;font-family:"Barlow",sans-serif;font-weight:700;font-size:18.5px;line-height:22px;color:var(--navy)}
.services svg{width:17px;height:17px;flex:none}
.closing{left:55px;top:403px;width:441px;font-size:16px;line-height:18.8px;text-align:justify}

.brand-small{left:50px;top:512px;font-size:13px;line-height:1.1;padding-bottom:6px;border-bottom:2px solid var(--rule)}
.brand-small .brand-mark{width:9px;height:30px}
.address{left:57px;top:570px;font-size:17px;line-height:20.5px}
.contact{left:57px;top:652px;font-size:17px;line-height:20.5px}
.contact b{font-weight:700}
.map{left:260px;top:520px;width:236px;height:174px;border:2px solid #111;border-radius:28px;background:linear-gradient(180deg,var(--map-tone-a),var(--map-tone-b))}
</style>
</head>
<body>
<section class="page page-front">
  <div class="abs brand brand-main"><span class="brand-mark"></span><span>Harborline Ambulatory<br>Surgery Center</span></div>
  <div class="abs header-rule"></div>
  <p class="abs intro"><span class="name">Harborline Ambulatory Surgery Center,</span> is a same day surgical center, conveniently located in the Bronx,licensed by the state of New York and accredited by NSAB</p>
  <div class="abs photo photo-building" role="img" aria-label="Street view of the surgery center building entrance"></div>
  <div class="abs photo photo-or" role="img" aria-label="Operating room with surgical table and equipment"></div>
  <h2 class="abs section-title loc-title">CONVENIENT LOCATION FOR PATIENTS AND SURGEONS</h2>
  <p class="abs section-body loc-body">Harborline Ambulatory Surgery Center is conveniently located on Alder Avenue in the Bronx, and is easily accessed from Manhattan, Westchester and Long Island with ample parking available on site.</p>
  <h2 class="abs section-title cap-title">CAPABILITIES OF HARBORLINE AMBULATORY SURGERY CENTER</h2>
  <p class="abs section-body cap-body">Harborline Ambulatory Surgery Centeris a dedicated facility for same day procedures that do not require an overnight hospital stay, without sacrificing the quality of care and safety that a hospital provides. Withover 15,000 sq ft of space and four operating rooms, the centeroffers specialties including orthopedics, pain management, podiatry, ophthalmology, ENT, pediatric ENT, and general surgery. These same day procedures, are performed by Harborline Ambulatory Surgery Center's highly skilled medical professionals that are committed to patient safety and satisfaction, providing the highest caliber of care with warmth and compassion in a personalized environment.</p>
</section>

<section class="page page-back">
  <p class="abs lead">More surgeons are choosing same day surgery centers because of the ability to provide high quality care in a state-of-the-art facility, at a more reasonable cost to you, your insurance provider, and your employer. Perhaps most importantly, same day surgery requires less down time, which means you'll spend less time away from your family and your job, and in most instances, you can return to your daily routine the next day.</p>
  <h2 class="abs offer-title">WE OFFER</h2>
  <ul class="abs services">
    <li><svg viewBox="0 0 17 17"><rect x="1" y="3" width="12" height="12" fill="none" stroke="#222" stroke-width="1.6"/><path d="M4 8l3 3 8-9" fill="none" stroke="#222" stroke-width="2"/></svg>ORTHOPEDICS</li>
    <li><svg viewBox="0 0 17 17"><rect x="1" y="3" width="12" height="12" fill="none" stroke="#222" stroke-width="1.6"/><path d="M4 8l3 3 8-9" fill="none" stroke="#222" stroke-width="2"/></svg>OPHTHALMOLOGY</li>
    <li><svg viewBox="0 0 17 17"><rect x="1" y="3" width="12" height="12" fill="none" stroke="#222" stroke-width="1.6"/><path d="M4 8l3 3 8-9" fill="none" stroke="#222" stroke-width="2"/></svg>PAIN MANAGEMENT</li>
    <li><svg viewBox="0 0 17 17"><rect x="1" y="3" width="12" height="12" fill="none" stroke="#222" stroke-width="1.6"/><path d="M4 8l3 3 8-9" fill="none" stroke="#222" stroke-width="2"/></svg>GENERAL SURGERY</li>
    <li><svg viewBox="0 0 17 17"><rect x="1" y="3" width="12" height="12" fill="none" stroke="#222" stroke-width="1.6"/><path d="M4 8l3 3 8-9" fill="none" stroke="#222" stroke-width="2"/></svg>ADULT &amp; PEDIATRIC ENT</li>
    <li><svg viewBox="0 0 17 17"><rect x="1" y="3" width="12" height="12" fill="none" stroke="#222" stroke-width="1.6"/><path d="M4 8l3 3 8-9" fill="none" stroke="#222" stroke-width="2"/></svg>PODIATRY</li>
  </ul>
  <p class="abs closing">Here at <b>Harborline Ambulatory Surgery Center</b>, the patient is our number one priority. To offer your patients the highest caliber care for same-day surgeries, contact Harborline Ambulatory Surgery Center today.</p>
  <div class="abs brand brand-small"><span class="brand-mark"></span><span>Harborline Ambulatory<br>Surgery Center</span></div>
  <p class="abs address">2840 Alder Avenue<br>Suite A,<br>Bronx, NY 10467</p>
  <p class="abs contact">Phone: <b>718-555-0142</b><br>Fax: <b>718-555-0143</b></p>
  <div class="abs map" role="img" aria-label="Location map of the surgery center"></div>
</section>
</body>
</html>
```